T&K Fleet Vans (HVAC business)

I'm looking to have our service trucks with a professional design. What we have now is too plain. I would like to keep the design simple but classy. I don't want any cartoon characters or any major logo modifications. I would like to stick with only red, black, and white as the colors of the project. Include phone numbers and website address on the truck. Plus descriptive words of our services. Please visit our website for ideas. www.tk-fleetair.com I am also attaching pictures of existing trucks we have already. I am willing to consider the truck wrap style of graphics, but not necessary I think. Sides and back are the pallet of the project. Thanks!
Updates

I am adding some blank pictures of the truck to the project. I have the contest guaranteed. Added Wednesday, July 12, 2017

Industry/Entity Type

Hvac

Requirements
Must have
• T&K logo, phone number, address

```html
<!DOCTYPE html>
<html lang="en">
<head>
<meta charset="utf-8">
<title>T&amp;K Fleet Vans – Service Van Graphics</title>
<link rel="stylesheet" href="https://fonts.googleapis.com/css2?family=Open+Sans:wght@700;800&display=swap">
<style>
  :root {
    --backdrop: #5a5858;
    --white: #ffffff;
    --ink: #1d1b1c;
    --red: #d3202b;
    --red-deep: #9b1019;
    --red-mid: #bd1822;
  }
  html, body {
    margin: 0;
    padding: 0;
    width: 831px;
    height: 1200px;
    overflow: hidden;
    background: var(--backdrop);
  }
  .canvas {
    position: relative;
    width: 831px;
    height: 1200px;
  }
  .van-side {
    position: absolute;
    display: block;
    background: var(--white);
  }
  .van-side--driver { left: 120px; top: 66px; width: 543px; height: 278px; }
  .van-side--passenger { left: 120px; top: 358px; width: 543px; height: 278px; }
  .van-rear { left: 145px; top: 649px; width: 492px; height: 489px; }
  .wordmark {
    font-family: "Open Sans", Arial, sans-serif;
    font-weight: 800;
    fill: var(--ink);
  }
  .services {
    font-family: "Open Sans", Arial, sans-serif;
    font-weight: 800;
    font-size: 15px;
    letter-spacing: 0.4px;
    fill: var(--ink);
  }
  .service-icon { fill: var(--red); }
  .contact {
    font-family: "Open Sans", Arial, sans-serif;
    font-weight: 800;
    fill: var(--white);
    text-anchor: middle;
  }
  .edge-line {
    fill: none;
    stroke: var(--ink);
    stroke-width: 2.2;
  }
</style>
</head>
<body>
<main class="canvas">

  <!-- Driver side -->
  <svg class="van-side van-side--driver" viewBox="0 0 588 301" aria-label="Van driver side graphic">
    <defs>
      <linearGradient id="redSweep" x1="0" y1="0" x2="1" y2="1">
        <stop offset="0" stop-color="#d52630"/>
        <stop offset="0.5" stop-color="#a8121b"/>
        <stop offset="1" stop-color="#cf1f29"/>
      </linearGradient>
    </defs>
    <path role="img" aria-label="Red faceted triangle pattern band" fill="url(#redSweep)"
          d="M0,65 Q330,205 588,76 L588,301 L370,301 Q150,250 0,133 Z"/>
    <path class="edge-line" d="M0,65 Q330,205 588,76"/>

    <text class="wordmark" x="160" y="78" font-size="56" text-anchor="middle">T&amp;K</text>
    <text class="wordmark" x="160" y="92" font-size="11" text-anchor="middle" letter-spacing="0.6">FLEET VANS</text>

    <g class="services">
      <rect class="service-icon" x="378" y="25" width="9" height="9"/>
      <text x="393" y="34">HEATING</text>
      <rect class="service-icon" x="378" y="43" width="9" height="9"/>
      <text x="393" y="52">COOLING</text>
      <rect class="service-icon" x="378" y="61" width="9" height="9"/>
      <text x="393" y="70">PLUMBING</text>
      <rect class="service-icon" x="378" y="80" width="9" height="9"/>
      <text x="393" y="89">REFRIGERATION</text>
    </g>

    <text class="contact" x="213" y="185" font-size="26">217-555-0148</text>
    <text class="contact" x="213" y="213" font-size="15">WWW.TK-FLEETAIR.COM</text>
    <text class="contact" x="510" y="164" font-size="19">EMERGENCY</text>
    <text class="contact" x="510" y="184" font-size="19">SERVICE</text>
  </svg>

  <!-- Passenger side -->
  <svg class="van-side van-side--passenger" viewBox="0 0 588 301" aria-label="Van passenger side graphic">
    <path role="img" aria-label="Red faceted triangle pattern band" fill="url(#redSweep)"
          d="M0,77 Q290,205 588,64 L588,134 Q450,250 230,301 L0,301 Z"/>
    <path class="edge-line" d="M0,77 Q290,205 588,64"/>

    <g class="services">
      <rect class="service-icon" x="82" y="21" width="9" height="9"/>
      <text x="97" y="30">HEATING</text>
      <rect class="service-icon" x="82" y="39" width="9" height="9"/>
      <text x="97" y="48">COOLING</text>
      <rect class="service-icon" x="82" y="57" width="9" height="9"/>
      <text x="97" y="66">PLUMBING</text>
      <rect class="service-icon" x="82" y="76" width="9" height="9"/>
      <text x="97" y="85">REFRIGERATION</text>
    </g>

    <text class="wordmark" x="434" y="74" font-size="56" text-anchor="middle">T&amp;K</text>
    <text class="wordmark" x="434" y="88" font-size="11" text-anchor="middle" letter-spacing="0.6">FLEET VANS</text>

    <text class="contact" x="76" y="156" font-size="19">EMERGENCY</text>
    <text class="contact" x="76" y="176" font-size="19">SERVICE</text>
    <text class="contact" x="369" y="181" font-size="26">217-555-0148</text>
    <text class="contact" x="369" y="212" font-size="15">WWW.TK-FLEETAIR.COM</text>
  </svg>

  <!-- Rear doors -->
  <svg class="van-side van-rear" viewBox="0 0 533 530" aria-label="Van rear doors graphic">
    <path role="img" aria-label="Red faceted triangle pattern panel" fill="url(#redSweep)"
          d="M0,205 Q300,170 533,125 L533,530 L0,530 Z"/>
    <path class="edge-line" d="M0,205 Q300,170 533,125"/>
    <path fill="var(--white)" d="M77,150 L173,150 L173,390 Q173,420 143,420 L107,420 Q77,420 77,390 Z"/>
    <path fill="var(--white)" d="M371,120 L467,120 L467,390 Q467,420 437,420 L401,420 Q371,420 371,390 Z"/>

    <text class="wordmark" x="266" y="90" font-size="72" text-anchor="middle">T&amp;K</text>
    <text class="wordmark" x="266" y="106" font-size="12" text-anchor="middle" letter-spacing="0.8">FLEET VANS</text>

    <text class="contact" x="273" y="469" font-size="35">217-555-0148</text>
    <text class="contact" x="273" y="500" font-size="21">WWW.TK-FLEETAIR.COM</text>
  </svg>

</main>
</body>
</html>
```